Solar Company Bussiness Card

I need a 2 sided business card and would like a .psd and any font files for each side of the card. I would like my logo used, it should be attached with the fonts. I'm not opposed to the font colors with the logo being changed.

On the sample design, I'd like the following:

Warren Kettle
President
Phone: 570-318-4957
www.brightvalepower.example

As I've recently opened in a 2nd market, I'm not sure about an address as I currently have 2 of them. I may actually get separate cards printed, one batch for each address, that's why I need the PSD file.
Updates

I'm very pleased with the response and designs I've received here for my business card. First and foremost, I'd like to thank everyone who took the time to submit a design. There truly are a lot of great designs in the bunch here and I'm having a little difficulty deciding. I will be reaching out to someone in the next day or two here to go to a final design. At this time, I'm not looking for any new concepts. If any of you do logos, I'm looking for a new logo for our sister entity, Kettle Partners, Inc. Thanks, Warren Kettle

Reason: I'm not looking for any new designs at this point, but extending this deadline in order to give people I've asked a chance to re-submit items.

```html
<!DOCTYPE html>
<html lang="en">
<head>
<meta charset="utf-8">
<title>Brightvale Power – Business Card</title>
<link rel="stylesheet" href="https://fonts.googleapis.com/css2?family=Fira+Sans:wght@400;500&display=swap">
<style>
  :root {
    --brand-dark: #0b5aa5;
    --brand-light: #3ba6e2;
    --card-edge: #6a97c6;
    --paper: #ffffff;
    --page: #ffffff;
  }
  * { margin: 0; padding: 0; box-sizing: border-box; }
  html, body {
    width: 849px;
    height: 1200px;
    overflow: hidden;
    background: var(--page);
    font-family: "Fira Sans", Arial, sans-serif;
  }
  .sheet {
    position: relative;
    width: 849px;
    height: 1200px;
  }
  .card {
    position: absolute;
    top: 808px;
    width: 387px;
    height: 226px;
    background: var(--paper);
    border: 1px solid var(--card-edge);
    overflow: hidden;
  }
  .card--front { left: 25px; }
  .card--back { left: 426px; }
  .card-waves {
    position: absolute;
    inset: 0;
    width: 100%;
    height: 100%;
  }
  .wave-dark { fill: var(--brand-dark); }
  .wave-light { fill: var(--brand-light); }

  .brand {
    position: absolute;
    left: 22px;
    top: 34px;
    display: flex;
    align-items: center;
    gap: 12px;
    color: var(--brand-dark);
    font-weight: 400;
  }
  .brand-mark {
    width: 40px;
    height: 40px;
    background: var(--brand-light);
  }
  .brand-name {
    font-size: 32px;
    line-height: 1;
    letter-spacing: 0.3px;
    white-space: nowrap;
  }

  .contact {
    position: absolute;
    left: 140px;
    top: 150px;
    list-style: none;
    color: var(--paper);
    font-size: 13px;
    font-weight: 400;
    line-height: 17.7px;
    letter-spacing: 0.4px;
    text-transform: uppercase;
    white-space: nowrap;
  }
</style>
</head>
<body>
<main class="sheet">

  <section class="card card--front" aria-label="Card front">
    <div class="brand">
      <span class="brand-mark" aria-hidden="true"></span>
      <span class="brand-name">Brightvale Power</span>
    </div>
    <svg class="card-waves" viewBox="0 0 387 226" preserveAspectRatio="none" aria-hidden="true">
      <path class="wave-light" d="M387 112 L387 132 C300 140 160 150 2 224 C130 160 260 128 387 112 Z"/>
      <path class="wave-dark" d="M2 224 C90 160 230 140 387 72 L387 114 C260 128 140 150 2 224 Z"/>
    </svg>
  </section>

  <section class="card card--back" aria-label="Card back">
    <svg class="card-waves" viewBox="0 0 387 226" preserveAspectRatio="none" aria-hidden="true">
      <path class="wave-light" d="M0 108 C80 104 150 118 230 110 C300 104 350 92 387 80 L387 226 L0 226 Z"/>
      <path class="wave-dark" d="M0 140 C80 128 180 118 260 110 C320 104 360 92 387 82 L387 226 L0 226 Z"/>
    </svg>
    <ul class="contact">
      <li>Warren Kettle</li>
      <li>President</li>
      <li>Phone: 570-318-4957</li>
      <li>www.brightvalepower.example</li>
    </ul>
  </section>

</main>
</body>
</html>
```